V Glowing Business Cards
Salon & Spa
Project: V Glowing Business Cards
V Glowing Business Cards - Salon & Spa
Creative Brief
Professional
Maribel Trostle
Owner
4100 Route 27 East Denville, NJ 07834
mtrostle@vglowingstudio.example
www.VGlowingstudio.example
we are looking for an elegant look and feel that is enticing and appealing for women of all ages (18-80 )

```html
<!DOCTYPE html>
<html lang="en">
<head>
<meta charset="utf-8">
<title>V Glowing Business Card</title>
<link href="https://fonts.googleapis.com/css2?family=Cinzel:wght@400;600&display=swap" rel="stylesheet">
<style>
  :root {
    --backdrop: #e9e7e4;
    --paper: #ffffff;
    --charcoal: #2e2e2e;
    --steel-light: #a8a8a8;
    --ink: #1f1f1f;
    --text-light: #f2f2f2;
    --text-muted: #b9b9b9;
  }
  html, body {
    margin: 0;
    width: 1200px;
    height: 900px;
    overflow: hidden;
    background: var(--backdrop);
  }
  .business-card {
    position: absolute;
    left: 110px;
    top: 170px;
    width: 980px;
    height: 560px;
    background: var(--paper);
    box-shadow: 0 18px 40px rgba(0,0,0,0.18);
    overflow: hidden;
    font-family: "Cinzel", Georgia, serif;
  }
  .card-shapes {
    position: absolute;
    inset: 0;
  }
  .brand-name {
    position: absolute;
    left: 70px;
    top: 96px;
    margin: 0;
    font-weight: 600;
    font-size: 64px;
    letter-spacing: 2px;
    color: var(--ink);
    line-height: 1;
  }
  .holder {
    position: absolute;
    right: 44px;
    top: 280px;
    text-align: right;
    color: var(--text-light);
  }
  .holder-name {
    font-size: 23px;
    letter-spacing: 1px;
  }
  .holder-role {
    margin-top: 4px;
    font-size: 13px;
    letter-spacing: 1.5px;
    color: var(--text-muted);
  }
  .contact-list {
    position: absolute;
    left: 52px;
    top: 392px;
    margin: 0;
    padding: 0;
    list-style: none;
    font-size: 16px;
    color: var(--text-light);
    letter-spacing: 0.5px;
  }
  .contact-item {
    display: flex;
    align-items: center;
    height: 27px;
    white-space: nowrap;
  }
  .contact-icon {
    width: 18px;
    height: 18px;
    margin-right: 9px;
    flex: none;
  }
  .contact-item.no-icon {
    padding-left: 27px;
  }
  .website {
    position: absolute;
    right: 44px;
    bottom: 17px;
    font-size: 14px;
    letter-spacing: 2px;
    color: var(--text-light);
  }
</style>
</head>
<body>
  <div class="business-card">
    <svg class="card-shapes" width="980" height="560" viewBox="0 0 980 560" aria-hidden="true">
      <defs>
        <linearGradient id="band-shade" x1="0" y1="0" x2="0" y2="1">
          <stop offset="0" stop-color="#333333"/>
          <stop offset="1" stop-color="#262626"/>
        </linearGradient>
        <linearGradient id="strip-shade" x1="0" y1="0" x2="1" y2="0">
          <stop offset="0" stop-color="#7c7c7c"/>
          <stop offset="1" stop-color="#9a9a9a"/>
        </linearGradient>
      </defs>
      <rect class="dark-band" x="0" y="250" width="980" height="310" fill="url(#band-shade)"/>
      <polygon class="band-notch" points="750,249 786,249 768,268" fill="var(--paper)"/>
      <path class="footer-strip" d="M400 560 C 450 560, 470 510, 540 508 L 980 508 L 980 560 Z" fill="url(#strip-shade)"/>
      <path class="footer-edge" d="M400 560 C 450 560, 470 510, 540 508 L 980 508" fill="none" stroke="var(--steel-light)" stroke-width="1.5"/>
    </svg>

    <h1 class="brand-name">V Glowing</h1>

    <div class="holder">
      <div class="holder-name">Maribel Trostle</div>
      <div class="holder-role">Owner</div>
    </div>

    <ul class="contact-list">
      <li class="contact-item">
        <svg class="contact-icon" viewBox="0 0 18 18" aria-hidden="true">
          <circle cx="9" cy="9" r="9" fill="var(--text-light)"/>
          <path d="M4.5 9.2 L9 5 L13.5 9.2 H12 V13 H10 V10.5 H8 V13 H6 V9.2 Z" fill="var(--charcoal)"/>
        </svg>
        4100 Route 27 East
      </li>
      <li class="contact-item no-icon">Marlow Falls, NJ 07999</li>
      <li class="contact-item">
        <svg class="contact-icon" viewBox="0 0 18 18" aria-hidden="true">
          <circle cx="9" cy="9" r="9" fill="var(--text-light)"/>
          <path d="M6 4.5 L7.6 4.5 L8.3 7 L7.2 7.9 C7.8 9.3 8.8 10.3 10.1 10.9 L11 9.8 L13.5 10.5 L13.5 12 C13.5 12.8 12.8 13.5 12 13.5 C8.4 13.2 4.8 9.6 4.5 6 C4.5 5.2 5.2 4.5 6 4.5 Z" fill="var(--charcoal)"/>
        </svg>
        973-555-0142
      </li>
      <li class="contact-item">
        <svg class="contact-icon" viewBox="0 0 18 18" aria-hidden="true">
          <circle cx="9" cy="9" r="9" fill="var(--text-light)"/>
          <rect x="4.5" y="6" width="9" height="6.5" fill="var(--charcoal)"/>
          <path d="M4.5 6 L9 9.6 L13.5 6" fill="none" stroke="var(--text-light)" stroke-width="1"/>
        </svg>
        mtrostle@vglowingstudio.example
      </li>
    </ul>

    <div class="website">www.VGlowingstudio.example</div>
  </div>
</body>
</html>
```